Unisex deodorant packaging

we need 12 designs of Unisex deodorant spray, all designs shoud be different.

Brand Name is Bremto. Artwork file size is attached for reference. Logo we can be redesigned.

variants names will be:

Pellimore
Quiln
Velontra
Morvik
Zantor
Pluvo
Ryxe
Omber
Sarevin
Tulpo
Vask
Dreen

Target Market(s)

B+, B, C+

Requirements
Must have
• colors, new fonts
Nice to have
• creative work, all 12 designs different

```html
<!DOCTYPE html>
<html lang="en">
<head>
<meta charset="utf-8">
<title>Bremto Pluvo – Deodorant Body Spray Label</title>
<link rel="stylesheet" href="https://fonts.googleapis.com/css2?family=Montserrat:wght@600&family=Kaushan+Script&family=Oswald:wght@600&display=swap">
<style>
  :root {
    --backdrop: #eef06e;
    --metal-light: #5a5c5f;
    --metal-dark: #2e2f31;
    --panel-brown: #3b312c;
    --panel-shade: #231d1a;
    --edge-silver: #c9cbce;
    --accent-yellow: #e6d22a;
    --text-white: #f2f2f2;
  }
  * { margin: 0; padding: 0; box-sizing: border-box; }
  html, body { width: 1200px; height: 1124px; overflow: hidden; }
  body { background: var(--backdrop); position: relative; }

  .label {
    position: absolute;
    left: 300px;
    top: 370px;
    width: 252px;
    height: 630px;
    border-radius: 0 0 10px 10px;
    overflow: hidden;
    background: linear-gradient(135deg, var(--metal-light), var(--metal-dark) 60%, #444548);
  }
  .label-art { position: absolute; inset: 0; }

  .brand-name {
    position: absolute;
    top: 42px;
    width: 100%;
    text-align: center;
    font-family: "Montserrat", sans-serif;
    font-weight: 600;
    font-size: 46px;
    line-height: 1;
    color: var(--text-white);
    letter-spacing: -1px;
  }

  .variant-name {
    position: absolute;
    top: 256px;
    width: 100%;
    text-align: center;
    font-family: "Oswald", sans-serif;
    font-weight: 600;
    font-size: 50px;
    line-height: 1;
    color: var(--accent-yellow);
    text-transform: uppercase;
    letter-spacing: 2px;
  }

  .product-type {
    position: absolute;
    left: 16px;
    top: 352px;
    width: 220px;
    transform: rotate(-10deg);
    font-family: "Kaushan Script", cursive;
    font-size: 30px;
    line-height: 1.15;
    color: var(--text-white);
    text-align: center;
  }

  .net-content {
    position: absolute;
    top: 570px;
    width: 100%;
    text-align: center;
    font-family: "Oswald", sans-serif;
    font-weight: 600;
    font-size: 19px;
    line-height: 1.2;
    color: var(--text-white);
  }
</style>
</head>
<body>
  <div class="label">
    <svg class="label-art" width="252" height="630" viewBox="0 0 252 630">
      <defs>
        <linearGradient id="panelFill" x1="0" y1="0" x2="1" y2="1">
          <stop offset="0" stop-color="#231d1a"/>
          <stop offset="0.5" stop-color="#3b312c"/>
          <stop offset="1" stop-color="#231d1a"/>
        </linearGradient>
      </defs>
      <polygon class="chevron-panel" points="0,62 252,190 252,458 104,534 0,458" fill="url(#panelFill)" role="img" aria-label="Dark brown perforated metal texture panel"/>
      <line class="chevron-edge" x1="0" y1="62" x2="252" y2="190" stroke="#c9cbce" stroke-width="3"/>
      <polyline class="chevron-edge" points="0,458 104,534 252,458" fill="none" stroke="#1a1a1b" stroke-width="3"/>
    </svg>

    <div class="brand-name">Bremto</div>

    <div class="variant-name">Pluvo</div>

    <div class="product-type">Deodorant<br>Body Spray</div>

    <div class="net-content">150ml Net 5.1 fl. oz.</div>
  </div>
</body>
</html>
```